Letterhead and Stationary for Construction Company

Brisk Current needs modern Letterhead, Envelopes and Notepad designs.

Industry/Entity Type

Construction

Colors
f78f20
34a7d8
ffffff

Requirements
Must have
• Modern looking design.

```html
<!DOCTYPE html>
<html lang="en">
<head>
<meta charset="utf-8">
<title>Brisk Current — Letterhead</title>
<link rel="stylesheet" href="https://fonts.googleapis.com/css2?family=Montserrat:wght@600&display=swap">
<style>
  :root {
    --backdrop: #000000;
    --paper: #ffffff;
    --brand-blue: #2878bd;
    --brand-orange: #e8832e;
    --tint-blue: #c3cfe6;
  }
  html, body {
    margin: 0;
    padding: 0;
    width: 1200px;
    height: 1197px;
    overflow: hidden;
    background: var(--backdrop);
  }
  .letterhead {
    position: absolute;
    left: 161px;
    top: 19px;
    width: 892px;
    height: 1154px;
    background: var(--paper);
    overflow: hidden;
  }
  .brand-dot {
    position: absolute;
    left: 26px;
    top: 33px;
    width: 100px;
    height: 100px;
    border-radius: 50%;
    background: var(--brand-orange);
  }
  .brand-name {
    position: absolute;
    left: 146px;
    top: 30px;
    margin: 0;
    font-family: "Montserrat", sans-serif;
    font-weight: 600;
    font-size: 50px;
    line-height: 48px;
    letter-spacing: -0.5px;
    color: var(--brand-blue);
  }
  .header-rule {
    position: absolute;
    left: 372px;
    top: 93px;
    width: 500px;
    height: 41px;
    background: var(--brand-blue);
  }
  .corner-accent {
    position: absolute;
    left: 0;
    top: 0;
    width: 892px;
    height: 1154px;
  }
</style>
</head>
<body>
  <main class="letterhead">
    <span class="brand-dot" aria-hidden="true"></span>
    <h1 class="brand-name">Brisk<br>Current</h1>

    <div class="header-rule" aria-hidden="true"></div>

    <svg class="corner-accent" viewBox="0 0 892 1154" aria-hidden="true">
      <circle cx="739" cy="990" r="241" fill="var(--tint-blue)" opacity="0.55"/>
    </svg>
  </main>
</body>
</html>
```